Fendrolique sanitzing wipes: logo, inner foil 6*8cm and consumer carton

we need a clever but simple logo design for a product and integrated look for the packaging (inner foil 6*8 cm and consumer carton). texts are provided for each and some examples of other products and formatting. we would use very simple imagery and color schemes. the main theme is safety, convenience, utility.

for the winning design we will for sure have some changes and adaptations and i would pay additionally for those.

Target Market(s)

American and European retail mass merchants -- wholesale stores, online, retail

Industry/Entity Type

Health And Wellness

Font styles to use
Sans Serif

Requirements
Must have
• Correct formatting of texts in accordance to regulations. Clear communication of texts in an easy to read and understandable formatting. Engaging, but simple design.
Nice to have
• Interesting use of color and contrast. some decent imagery/visual graphics that can make the outter packaging pop on shelf.
Should not have
• odd fonts or formatting. knock-offs of other designs of a similar product in its category, cliché or overused imagery

```html
<!DOCTYPE html>
<html lang="en">
<head>
<meta charset="utf-8">
<title>Sanitizing Wipe Sachet – Drug Facts</title>
<link rel="stylesheet" href="https://fonts.googleapis.com/css2?family=Questrial&display=swap">
<style>
  :root {
    --backdrop: #aee9e6;
    --foil: #efefef;
    --foil-edge: #e2e2e2;
    --crimp: #d6d6d6;
    --ink: #111111;
    --green: #1f8a44;
    --rule: #1a1a1a;
  }
  * { box-sizing: border-box; margin: 0; padding: 0; }
  html, body {
    width: 1200px; height: 857px; overflow: hidden;
    background: var(--backdrop);
    font-family: "Questrial", "Helvetica Neue", Arial, sans-serif;
    color: var(--ink);
  }
  .sachet {
    position: absolute; left: 330px; top: 24px;
    width: 540px; height: 809px;
    background: linear-gradient(160deg, #f7f7f7 0%, var(--foil) 55%, #e6e6e6 100%);
    border: 1px solid var(--foil-edge);
    border-radius: 4px;
  }
  .sachet-crimp {
    position: absolute; top: 18px; bottom: 18px; width: 34px;
  }
  .sachet-crimp--left { left: 10px; }
  .sachet-crimp--right { right: 10px; }
  .sachet-crimp svg { width: 100%; height: 100%; display: block; }

  .drug-facts {
    position: absolute; left: 62px; top: 58px;
    width: 416px; height: 694px;
    border: 3px solid var(--rule);
    background: rgba(255,255,255,0.55);
  }
  .panel-section {
    border-bottom: 2.5px solid var(--rule);
    padding: 8px 14px 9px;
  }
  .panel-section:last-child { border-bottom: none; }
  .panel-title {
    color: var(--green);
    font-size: 28px; font-weight: 400; letter-spacing: 0.3px;
    line-height: 1.05;
  }
  .section-title {
    color: var(--green);
    font-size: 26px; line-height: 1.1;
    border-bottom: 1px solid var(--rule);
    padding-bottom: 2px; margin-bottom: 5px;
  }
  .facts-header {
    display: flex; justify-content: space-between; align-items: flex-end;
    border-top: 1px solid var(--rule);
    margin-top: 4px; padding-top: 4px;
    font-size: 17px;
  }
  .ingredient-row {
    display: flex; align-items: baseline;
    font-size: 14px; margin-top: 4px;
  }
  .ingredient-row .leader {
    flex: 1; border-bottom: 1.5px dotted var(--ink); margin: 0 3px; transform: translateY(-3px);
  }
  .fact-list { list-style: none; font-size: 14px; line-height: 1.32; }
  .fact-list li { position: relative; padding-left: 16px; margin-bottom: 2px; }
  .fact-list li::before {
    content: ""; position: absolute; left: 1px; top: 5px;
    width: 9px; height: 9px; border-radius: 50%; background: var(--green);
  }
  .fact-list .note { display: block; padding-left: 6px; }
</style>
</head>
<body>
  <div class="sachet">
    <div class="sachet-crimp sachet-crimp--left" aria-hidden="true">
      <svg viewBox="0 0 34 100" preserveAspectRatio="none">
        <g stroke="var(--crimp)" stroke-width="1.2" vector-effect="non-scaling-stroke">
          <line x1="4" y1="0" x2="4" y2="100"/><line x1="10" y1="0" x2="10" y2="100"/>
          <line x1="16" y1="0" x2="16" y2="100"/><line x1="22" y1="0" x2="22" y2="100"/>
          <line x1="28" y1="0" x2="28" y2="100"/>
        </g>
      </svg>
    </div>
    <div class="sachet-crimp sachet-crimp--right" aria-hidden="true">
      <svg viewBox="0 0 34 100" preserveAspectRatio="none">
        <g stroke="var(--crimp)" stroke-width="1.2" vector-effect="non-scaling-stroke">
          <line x1="6" y1="0" x2="6" y2="100"/><line x1="12" y1="0" x2="12" y2="100"/>
          <line x1="18" y1="0" x2="18" y2="100"/><line x1="24" y1="0" x2="24" y2="100"/>
          <line x1="30" y1="0" x2="30" y2="100"/>
        </g>
      </svg>
    </div>

    <section class="drug-facts">
      <div class="panel-section">
        <h1 class="panel-title">Drug Facts</h1>
        <div class="facts-header"><span>Active Ingredient</span><span>Purpose</span></div>
        <ul class="fact-list">
          <li class="ingredient-row" style="padding-left:16px">Ethyl Alcohol 75%<span class="leader"></span>Antimicrobial</li>
        </ul>
      </div>
      <div class="panel-section">
        <h2 class="section-title">Use</h2>
        <ul class="fact-list">
          <li>Hand Sanitizer – To decrease bacteria on the skin that can cause disease.</li>
        </ul>
      </div>
      <div class="panel-section">
        <h2 class="section-title">Warnings</h2>
        <ul class="fact-list">
          <li>Flammable: Keep away from fire or flames.</li>
          <li>For external use only: Hands only. Do not use on face or eyes or if you are allergic to any ingredients.</li>
          <li>When using this product keep away from and out of eyes. In case of contact with eyes, flush thoroughly with water * avoid contact with broken skin.<span class="note">* Do not inhale or ingest.</span></li>
          <li>Stop use and ask a doctor should irritation or redness appear and persist for 72 hours.</li>
          <li>Keep out of reach of children. If swallowed, get medical help or contact a Poison Control Center right away.</li>
        </ul>
      </div>
      <div class="panel-section">
        <h2 class="section-title">Directions</h2>
        <ul class="fact-list">
          <li>Wipe hands thoroughly with product and allow to dry. For children under 6, use only under adult supervision.</li>
        </ul>
      </div>
    </section>
  </div>
</body>
</html>
```